Business Card Design Project

I need a business card design for an Organic drive thru coffee kiosk. We will serve organic coffee, teas & smoothies and will serve healthy breakfast food/snacks for people on the go.
I want the card to have 2-3 colors max (earthy colors like browns, greens and so on).
I have attached the logo I want used and would love to play off the theme of "balance."
Include:
Tidy-Kettle Coffee
address: 4820 Gorvin Ct. Raleigh, NC 27583
phone: 919-731-4062
website: www.tidy-kettle.com (website is not up yet but still include it on card)
email: Rosalind@tidy-kettle.com
I want one of the following sayings somewhere on the card (the front or back is fine):
"Eat & Drink Well, on the run!"
"Break the fast with Tidy-Kettle"
Maybe on the back list what we offer:
-Organic coffee, espresso & tea
-Blendora smoothies & protein shakes
-Zesty Pour (100% fresh local fruit and veggies)
-Tender Nibs

```html
<!DOCTYPE html>
<html lang="en">
<head>
<meta charset="utf-8">
<title>Tidy-Kettle Coffee – Business Card</title>
<link rel="stylesheet" href="https://fonts.googleapis.com/css2?family=Source+Sans+3:wght@400;600&display=swap">
<style>
  :root {
    --page: #ece6dc;
    --card: #e4c690;
    --brown: #4a2a14;
    --green: #8cba2c;
    --icon-green: #6f9a25;
    --white: #ffffff;
  }
  * { margin: 0; padding: 0; box-sizing: border-box; }
  html, body { width: 1200px; height: 1200px; overflow: hidden; }
  body {
    background: var(--page);
    font-family: "Source Sans 3", sans-serif;
    color: var(--brown);
    position: relative;
  }
  .card {
    position: absolute;
    left: 150px;
    width: 900px;
    height: 514px;
    background: var(--card);
    overflow: hidden;
    box-shadow: 0 6px 18px rgba(60, 40, 20, 0.25);
  }
  .card--front { top: 40px; }
  .card--back { top: 646px; }

  /* Front */
  .brand {
    position: absolute;
    left: 250px;
    top: 110px;
    display: flex;
    align-items: center;
    gap: 18px;
  }
  .brand__dot {
    width: 44px; height: 44px;
    border-radius: 50%;
    background: var(--brown);
  }
  .brand__name {
    font-size: 64px;
    font-weight: 600;
    color: var(--brown);
    letter-spacing: 0.5px;
  }
  .contact {
    position: absolute;
    left: 150px;
    top: 250px;
    list-style: none;
  }
  .contact__item {
    display: flex;
    align-items: center;
    gap: 10px;
    font-size: 36px;
    line-height: 52px;
  }
  .icon { width: 32px; height: 32px; flex: none; }

  /* Back */
  .bands { position: absolute; inset: 0; }
  .tagline {
    position: absolute;
    left: 40px;
    top: 50px;
    font-size: 44px;
    color: var(--white);
    transform: rotate(2.5deg);
    transform-origin: left center;
  }
  .offer-list {
    position: absolute;
    left: 250px;
    top: 180px;
    list-style: none;
    font-size: 34px;
    line-height: 40px;
    text-align: center;
  }
  .web {
    position: absolute;
    left: 60px;
    top: 400px;
    display: flex;
    align-items: center;
    gap: 12px;
    font-size: 38px;
  }
</style>
</head>
<body>

<section class="card card--front">
  <div class="brand">
    <span class="brand__dot"></span>
    <span class="brand__name">Tidy-Kettle</span>
  </div>
  <ul class="contact">
    <li class="contact__item">
      <svg class="icon" viewBox="0 0 32 32" aria-hidden="true"><circle cx="16" cy="16" r="14" fill="none" stroke="var(--icon-green)" stroke-width="3"/><path d="M9 16 L16 9 L23 16 M11 15 V23 H21 V15" fill="none" stroke="var(--brown)" stroke-width="2.2"/></svg>
      4820 Gorvin Ct. Raleigh, NC 27583
    </li>
    <li class="contact__item">
      <svg class="icon" viewBox="0 0 32 32" aria-hidden="true"><circle cx="16" cy="16" r="14" fill="none" stroke="var(--icon-green)" stroke-width="3"/><path d="M11 9 L14 9 L15 13 L13 15 Q15 19 18 20 L20 18 L23 19 L23 22 Q15 24 10 13 Z" fill="var(--brown)"/></svg>
      919-731-4062
    </li>
    <li class="contact__item">
      <svg class="icon" viewBox="0 0 32 32" aria-hidden="true"><circle cx="16" cy="16" r="14" fill="none" stroke="var(--icon-green)" stroke-width="3"/><circle cx="17" cy="14" r="5" fill="none" stroke="var(--brown)" stroke-width="2.4"/><path d="M13 18 L9 22" stroke="var(--brown)" stroke-width="3"/></svg>
      www.tidy-kettle.com
    </li>
    <li class="contact__item">
      <svg class="icon" viewBox="0 0 32 32" aria-hidden="true"><circle cx="16" cy="16" r="14" fill="none" stroke="var(--icon-green)" stroke-width="3"/><rect x="9" y="11" width="14" height="10" fill="none" stroke="var(--brown)" stroke-width="2"/><path d="M9 11 L16 17 L23 11" fill="none" stroke="var(--brown)" stroke-width="2"/></svg>
      Rosalind@tidy-kettle.com
    </li>
  </ul>
</section>

<section class="card card--back">
  <svg class="bands" viewBox="0 0 900 514" preserveAspectRatio="none" aria-hidden="true">
    <polygon points="0,40 900,82 900,170 0,95" fill="var(--green)"/>
    <polygon points="0,330 900,372 900,514 0,514" fill="var(--white)"/>
    <rect x="0" y="470" width="900" height="44" fill="var(--card)"/>
  </svg>
  <p class="tagline">Break the fast with Tidy-Kettle</p>
  <ul class="offer-list">
    <li>-Organic coffee, espresso &amp; tea</li>
    <li>-Blendora smoothies &amp; protein shakes</li>
    <li>-Zesty Pour (100% fresh local fruit and veggies)</li>
    <li>-Tender Nibs</li>
  </ul>
  <div class="web">
    <svg class="icon" viewBox="0 0 32 32" aria-hidden="true"><circle cx="16" cy="16" r="14" fill="none" stroke="var(--icon-green)" stroke-width="3"/><circle cx="17" cy="14" r="5" fill="none" stroke="var(--brown)" stroke-width="2.4"/><path d="M13 18 L9 22" stroke="var(--brown)" stroke-width="3"/></svg>
    www.tidy-kettle.com
  </div>
</section>

</body>
</html>
```